Wanted banner ads for website

For our new advertising page we need 10 meaningful advertising banners that match the new website. The banners are required as sliders for the new site.

The image material can be used directly from the website.

The banners must have a size of 850x280 PIXELS. The new website can be found at www.varnimo.net

The following banners should be created.

1. quickLoan (sample attached)
2. https://www.varnimo.net/product_info.php?products_id=1464
3. https://www.varnimo.net/product_info.php?products_id=110992
4. https://www.varnimo.net/product_info.php?products_id=1691
4. https://www.varnimo.net/product_info.php?products_id=118371
5. https://www.varnimo.net/product_info.php?products_id=139042
6. https://www.varnimo.net/product_info.php?products_id=242175
7. https://www.varnimo.net/product_info.php?products_id=140105
8. https://www.varnimo.net/product_info. php?products_id=140156
9. https://www.varnimo.net/product_info.php?products_id=139722
10. https://www.varnimo.net/product_info.php?products_id=140175

```html
<!DOCTYPE html>
<html lang="en">
<head>
<meta charset="utf-8">
<title>Varnimo slider banners</title>
<link rel="stylesheet" href="https://fonts.googleapis.com/css2?family=Oswald:wght@500;700&family=Roboto:wght@400;700&display=swap">
<style>
:root{
  --page:#e9eaee;
  --navy:#0b1440;
  --navy-deep:#050a26;
  --royal:#1d3fb8;
  --violet:#4a1a9e;
  --magenta:#c0177e;
  --plum:#5a0d4a;
  --red:#e3172b;
  --sky:#2aa7ff;
  --white:#ffffff;
  --ink:#10142b;
  --lime:#39e07a;
}
*{box-sizing:border-box;margin:0;padding:0}
html,body{width:795px;height:1200px;overflow:hidden;background:var(--page)}
body{font-family:"Roboto",Arial,sans-serif;color:var(--white)}
.sheet{
  position:absolute;left:21px;top:22px;
  display:grid;grid-template-columns:371px 371px;grid-auto-rows:104px;
  column-gap:11px;row-gap:13px;
}
.banner{position:relative;overflow:hidden;border-radius:2px}
.brand{
  position:absolute;left:8px;top:7px;display:flex;align-items:center;gap:4px;z-index:2;
  font:700 9px "Roboto",Arial,sans-serif;color:var(--white);letter-spacing:.3px
}
.brand-dot{width:15px;height:15px;border-radius:50%;border:2px solid var(--white)}
.photo{position:absolute;border-radius:4px}
.title{
  position:absolute;font-family:"Oswald",Arial,sans-serif;font-weight:700;
  text-transform:uppercase;line-height:1.15;font-size:10px;white-space:nowrap
}
.specs{
  position:absolute;list-style:none;font-size:6px;line-height:1.45;white-space:nowrap;
  padding:4px 6px;border:1px solid rgba(255,255,255,.7);border-radius:3px
}
.tag{
  position:absolute;font:700 7px "Roboto",Arial,sans-serif;text-transform:uppercase;
  padding:3px 6px;border-radius:2px;line-height:1.3;white-space:nowrap
}
.maker{position:absolute;font:700 16px "Oswald",Arial,sans-serif;letter-spacing:1px;line-height:1.2}

/* left column layout: text left, product right */
.layout-left .title{left:60px;top:28px}
.layout-left .specs{left:60px;top:58px;width:130px}
.layout-left .photo{right:12px;top:12px;width:118px;height:80px}

/* right column layout: product left, text right */
.layout-right .photo{left:80px;top:12px;width:100px;height:80px}
.layout-right .title{left:192px;top:12px}
.layout-right .tag{left:192px;top:50px}
.layout-right .maker{left:192px;top:68px}

/* themes */
.theme-washer{background:linear-gradient(120deg,var(--navy-deep) 0 45%,var(--royal) 45% 70%,var(--navy) 70%)}
.theme-washer .photo{background:radial-gradient(circle at 45% 50%,#ffd84a 0 12%,#e3172b 25%,#1a1a2a 60%)}

.theme-partybar{background:linear-gradient(110deg,#0a1a5a 0 40%,#2450d8 60%,#0a1a5a)}
.theme-partybar .photo{background:linear-gradient(90deg,#1b1f33,#5b6aa8 50%,#1b1f33)}

.theme-bullets{background:linear-gradient(100deg,var(--navy-deep) 0 35%,var(--violet) 35% 62%,#25106b 62%)}
.theme-bullets .photo{background:radial-gradient(circle at 40% 50%,#33d48b 0 14%,#d2335a 28%,#2a2540 62%)}

.theme-par{background:linear-gradient(115deg,var(--plum) 0 40%,var(--magenta) 40% 62%,#3a0b5c 62%)}
.theme-par .photo{background:radial-gradient(circle at 45% 50%,var(--lime) 0 18%,#1e3a2c 55%,#141421)}

.theme-case{background:linear-gradient(110deg,var(--white) 0 52%,var(--royal) 52% 70%,var(--navy) 70%)}
.theme-case .title{color:var(--red)}
.theme-case .brand{color:var(--ink)}
.theme-case .brand-dot{border-color:var(--ink)}
.theme-case .specs{color:var(--ink);border-color:var(--ink)}
.theme-case .photo{background:linear-gradient(135deg,#222632,#545a6b)}

.theme-movinghead{background:linear-gradient(115deg,var(--navy-deep) 0 55%,var(--navy) 55%)}
.theme-movinghead .title{color:var(--red)}
.theme-movinghead .photo{background:radial-gradient(circle at 50% 50%,#ffe066 0 10%,#e3172b 26%,#1a1a26 62%)}
.theme-movinghead .tag{background:var(--red)}

.theme-panel{background:linear-gradient(115deg,#0f0b3a 0 40%,#4b1fc0 40% 65%,#1a0f5e 65%)}
.theme-panel .photo{background:linear-gradient(135deg,#c42a3a,#2a1a3a)}
.theme-panel .tag{background:var(--magenta)}

.theme-truss{background:linear-gradient(110deg,#090a1e 0 45%,#1d1f4d 45% 70%,#0d0f2c 70%)}
.theme-truss .photo{background:linear-gradient(135deg,#2e3240,#8a8f9e 50%,#2e3240)}
.theme-truss .tag{background:var(--sky)}

.theme-speaker{background:linear-gradient(110deg,#07123e 0 50%,#0e2b8f 50% 75%,#07123e 75%)}
.theme-speaker .photo{background:radial-gradient(circle at 50% 45%,#2aa7ff 0 14%,#111420 45%)}
.theme-speaker .tag{background:var(--red)}

.theme-active{background:linear-gradient(110deg,#0a0c18 0 50%,#1d2034 50%)}
.theme-active .photo{background:linear-gradient(135deg,#16171f,#3c3f4f)}
.theme-active .tag{background:var(--red)}
.theme-active .maker{color:var(--red)}
</style>
</head>
<body>
<main class="sheet">

  <article class="banner layout-left theme-washer">
    <div class="brand"><span class="brand-dot"></span>varnimo</div>
    <h2 class="title">Lumex LED Moving Head<br>Washer 7x12 with Zoom</h2>
    <ul class="specs"><li>7 x 12 W RGBW LEDs</li><li>Zoom 10° to 60°</li><li>DMX, auto and sound modes</li></ul>
    <div class="photo" role="img" aria-label="LED moving head washer product photo"></div>
  </article>
  <article class="banner layout-right theme-movinghead">
    <div class="brand"><span class="brand-dot"></span>varnimo</div>
    <div class="photo" role="img" aria-label="LED moving head product photo"></div>
    <h2 class="title">Lumex LED Moving Head<br>Beam Spot 60 W</h2>
    <p class="tag">Now available online</p>
    <p class="maker">LUMEX</p>
  </article>

  <article class="banner layout-left theme-washer">
    <div class="brand"><span class="brand-dot"></span>varnimo</div>
    <h2 class="title">Lumex LED Moving Head<br>Washer 7x12 with Zoom</h2>
    <ul class="specs"><li>7 x 12 W RGBW LEDs</li><li>Zoom 10° to 60°</li><li>DMX, auto and sound modes</li></ul>
    <div class="photo" role="img" aria-label="LED moving head washer product photo"></div>
  </article>
  <article class="banner layout-right theme-movinghead">
    <div class="brand"><span class="brand-dot"></span>varnimo</div>
    <div class="photo" role="img" aria-label="LED moving head product photo"></div>
    <h2 class="title">Lumex LED Moving Head<br>Beam Spot 60 W</h2>
    <p class="tag">Now available online</p>
    <p class="maker">LUMEX</p>
  </article>

  <article class="banner layout-left theme-partybar">
    <div class="brand"><span class="brand-dot"></span>varnimo</div>
    <h2 class="title">Lumex LED Partybar</h2>
    <ul class="specs"><li>4 x PAR spots with stand</li><li>Foot switch and remote</li><li>Ready to play in minutes</li></ul>
    <div class="photo" role="img" aria-label="LED partybar on stand product photo"></div>
  </article>
  <article class="banner layout-right theme-panel">
    <div class="brand"><span class="brand-dot"></span>varnimo</div>
    <div class="photo" role="img" aria-label="LED panel fixture product photo"></div>
    <h2 class="title">Korva Panel with<br>Power Bus Plus</h2>
    <p class="tag">Pro stage panel</p>
    <p class="maker">KORVA</p>
  </article>

  <article class="banner layout-left theme-partybar">
    <div class="brand"><span class="brand-dot"></span>varnimo</div>
    <h2 class="title">Lumex LED Partybar</h2>
    <ul class="specs"><li>4 x PAR spots with stand</li><li>Foot switch and remote</li><li>Ready to play in minutes</li></ul>
    <div class="photo" role="img" aria-label="LED partybar on stand product photo"></div>
  </article>
  <article class="banner layout-right theme-panel">
    <div class="brand"><span class="brand-dot"></span>varnimo</div>
    <div class="photo" role="img" aria-label="LED panel fixture product photo"></div>
    <h2 class="title">Korva Panel with<br>Power Bus Plus</h2>
    <p class="tag">Pro stage panel</p>
    <p class="maker">KORVA</p>
  </article>

  <article class="banner layout-left theme-bullets">
    <div class="brand"><span class="brand-dot"></span>varnimo</div>
    <h2 class="title">Lumex LED Bullets<br>Moving Head 7x15 W</h2>
    <ul class="specs"><li>Endless pan and tilt</li><li>RGBW colour mixing</li></ul>
    <div class="photo" role="img" aria-label="LED bullets moving head product photo"></div>
  </article>
  <article class="banner layout-right theme-truss">
    <div class="brand"><span class="brand-dot"></span>varnimo</div>
    <div class="photo" role="img" aria-label="Lighting truss system product photo"></div>
    <h2 class="title">Korva LED Bar<br>with Truss Mount</h2>
    <p class="tag">Order today</p>
    <p class="maker">KORVA</p>
  </article>

  <article class="banner layout-left theme-bullets">
    <div class="brand"><span class="brand-dot"></span>varnimo</div>
    <h2 class="title">Lumex LED Bullets<br>Moving Head 7x15 W</h2>
    <ul class="specs"><li>Endless pan and tilt</li><li>RGBW colour mixing</li></ul>
    <div class="photo" role="img" aria-label="LED bullets moving head product photo"></div>
  </article>
  <article class="banner layout-right theme-truss">
    <div class="brand"><span class="brand-dot"></span>varnimo</div>
    <div class="photo" role="img" aria-label="Lighting truss system product photo"></div>
    <h2 class="title">Korva LED Bar<br>with Truss Mount</h2>
    <p class="tag">Order today</p>
    <p class="maker">KORVA</p>
  </article>

  <article class="banner layout-left theme-par">
    <div class="brand"><span class="brand-dot"></span>varnimo</div>
    <h2 class="title">Lumex LED Par Flat<br>RGBW 12x8 W Wireless</h2>
    <ul class="specs"><li>Battery powered</li><li>Wireless DMX built in</li></ul>
    <div class="photo" role="img" aria-label="Battery LED par light product photo"></div>
  </article>
  <article class="banner layout-right theme-speaker">
    <div class="brand"><span class="brand-dot"></span>varnimo</div>
    <div class="photo" role="img" aria-label="Party speaker with lights product photo"></div>
    <h2 class="title">Sonara Party Speaker<br>with LED Effects</h2>
    <p class="tag">Bluetooth · USB · Mic in</p>
    <p class="maker">SONARA</p>
  </article>

  <article class="banner layout-left theme-par">
    <div class="brand"><span class="brand-dot"></span>varnimo</div>
    <h2 class="title">Lumex LED Par Flat<br>RGBW 12x8 W Wireless</h2>
    <ul class="specs"><li>Battery powered</li><li>Wireless DMX built in</li></ul>
    <div class="photo" role="img" aria-label="Battery LED par light product photo"></div>
  </article>
  <article class="banner layout-right theme-speaker">
    <div class="brand"><span class="brand-dot"></span>varnimo</div>
    <div class="photo" role="img" aria-label="Party speaker with lights product photo"></div>
    <h2 class="title">Sonara Party Speaker<br>with LED Effects</h2>
    <p class="tag">Bluetooth · USB · Mic in</p>
    <p class="maker">SONARA</p>
  </article>

  <article class="banner layout-left theme-case">
    <div class="brand"><span class="brand-dot"></span>varnimo</div>
    <h2 class="title">Lumex Flight Case<br>for Moving Heads</h2>
    <ul class="specs"><li>Wheels and foam inlay</li><li>Fits two fixtures</li></ul>
    <div class="photo" role="img" aria-label="Flight case product photo"></div>
  </article>
  <article class="banner layout-right theme-active">
    <div class="brand"><span class="brand-dot"></span>varnimo</div>
    <div class="photo" role="img" aria-label="Active two way speaker box product photo"></div>
    <h2 class="title">Sonara Active 2 Way<br>Speaker Box 15"</h2>
    <p class="tag">800 W peak power</p>
    <p class="maker">SONARA</p>
  </article>

  <article class="banner layout-left theme-case">
    <div class="brand"><span class="brand-dot"></span>varnimo</div>
    <h2 class="title">Lumex Flight Case<br>for Moving Heads</h2>
    <ul class="specs"><li>Wheels and foam inlay</li><li>Fits two fixtures</li></ul>
    <div class="photo" role="img" aria-label="Flight case product photo"></div>
  </article>
  <article class="banner layout-right theme-active">
    <div class="brand"><span class="brand-dot"></span>varnimo</div>
    <div class="photo" role="img" aria-label="Active two way speaker box product photo"></div>
    <h2 class="title">Sonara Active 2 Way<br>Speaker Box 15"</h2>
    <p class="tag">800 W peak power</p>
    <p class="maker">SONARA</p>
  </article>

</main>
</body>
</html>
```